BLUE FORGE (Business Card for Training Company)

Blue Forge is a training and consultancy company with a focus on executive protection and medical. I would like the card to be nice and sharp, not overdone and in black and red. I would also like it to highlight that it is "A Tavmont Company"

I would like it to be simple and highlight a few things.

1. Name
2. Title
3. Phone Number
4. Email

I would also like www.tavmontgroup.example/blue-forge to be on the card somewhere.

Target Market(s)

Security Companies

Industry/Entity Type

Security

Contact Information for Business Card

Blue Forge is a training and consultancy company with a focus on executive protection and medical. I would like the card to be nice and sharp, not overdone and in black and red. I would also like it to highlight that it is "A Tavmont Company" I would like it to be simple and highlight a few things. 1. Name 2. Title 3. Phone Number 4. Email I would also like www.tavmontgroup.example/blue-forge to be on the card somewhere.

Requirements
Must have
• A Tavmont Company listed on the card and the website
Nice to have
• Highlight Medical Training, Consultancy & Executive Protection Courses

```html
<!DOCTYPE html>
<html lang="en">
<head>
<meta charset="utf-8">
<title>Blue Forge — Business Card</title>
<link href="https://fonts.googleapis.com/css2?family=Arimo:wght@400;700&display=swap" rel="stylesheet">
<style>
  :root {
    --backdrop: #111112;
    --card: #2a2a2c;
    --edge: #8e1116;
    --ink: #ffffff;
    --ink-soft: #e6e6e6;
    --rule: #5a5a5d;
    --accent: #a3141b;
    --deboss: #3c3c3f;
  }
  * { box-sizing: border-box; margin: 0; padding: 0; }
  html, body {
    width: 1200px; height: 820px; overflow: hidden;
    background: var(--backdrop);
    font-family: "Arimo", Arial, sans-serif;
  }
  .sheet {
    width: 1200px; height: 820px;
    display: flex; align-items: center; justify-content: center; gap: 40px;
  }
  .card {
    position: relative;
    width: 540px; height: 309px;
    background: var(--card);
    border-bottom: 3px solid var(--edge);
    border-right: 2px solid var(--edge);
    box-shadow: 0 18px 40px rgba(0,0,0,.6);
    color: var(--ink);
  }
  /* Front */
  .card-front .brand {
    position: absolute; left: 232px; top: 42px;
    font-weight: 700; font-size: 54px; line-height: 0.9;
    letter-spacing: 1px; color: var(--ink);
  }
  .card-front .divider {
    position: absolute; left: 232px; top: 168px;
    width: 236px; height: 1px; background: var(--rule);
  }
  .contact {
    position: absolute; left: 34px; top: 190px;
  }
  .contact .person-name {
    font-weight: 700; font-size: 21px; letter-spacing: .5px; line-height: 1;
  }
  .contact .person-title {
    font-size: 14px; color: var(--ink-soft); margin-top: 3px;
  }
  .contact .line {
    display: flex; align-items: center; gap: 8px;
    font-size: 14px; color: var(--ink-soft); margin-top: 6px;
  }
  .contact .line svg { width: 14px; height: 14px; flex: none; }
  .contact .website {
    font-size: 14px; color: var(--ink-soft); margin-top: 12px;
  }
  .parent {
    position: absolute; right: 50px; top: 198px; text-align: left;
  }
  .parent .parent-tagline {
    font-size: 14px; letter-spacing: .5px; color: var(--ink);
  }
  .parent .parent-name {
    display: flex; align-items: center; gap: 8px; margin-top: 8px;
    font-weight: 700; font-size: 22px; color: var(--ink);
  }
  .parent .parent-name .mark {
    width: 20px; height: 20px; background: var(--accent);
  }
  /* Back */
  .card-back .brand {
    position: absolute; left: 0; right: 0; top: 62px; text-align: center;
    font-weight: 700; font-size: 58px; line-height: 0.9; letter-spacing: 1px;
    color: var(--deboss);
  }
  .services {
    position: absolute; left: 0; right: 0; bottom: 44px;
    display: flex; justify-content: center; align-items: center; gap: 8px;
    font-size: 15px; color: var(--ink-soft);
  }
  .services .dot {
    width: 6px; height: 6px; border-radius: 50%; background: var(--accent);
  }
</style>
</head>
<body>
<main class="sheet">
  <section class="card card-front" aria-label="Card front">
    <div class="brand">BLUE<br>FORGE</div>
    <div class="divider"></div>
    <div class="contact">
      <p class="person-name">DANIEL HARTLEY</p>
      <p class="person-title">Managing Director</p>
      <p class="line">
        <svg viewBox="0 0 16 16" aria-hidden="true"><path d="M4 1.5l2.2 2.6-1.3 1.6c.9 2 2.4 3.5 4.4 4.4l1.6-1.3 2.6 2.2-1.4 2.4C7 13.4 2.6 9 1.6 2.9z" fill="none" stroke="#fff" stroke-width="1.3" stroke-linejoin="round"/></svg>
        044-555 018 342
      </p>
      <p class="line">
        <svg viewBox="0 0 16 16" aria-hidden="true"><rect x="1.5" y="3.5" width="13" height="9" fill="none" stroke="#fff" stroke-width="1.3"/><path d="M1.5 3.5L8 9l6.5-5.5" fill="none" stroke="#fff" stroke-width="1.3"/></svg>
        info@blueforge.example
      </p>
      <p class="website">www.tavmontgroup.example/blue-forge</p>
    </div>
    <div class="parent">
      <p class="parent-tagline">A TAVMONT COMPANY</p>
      <p class="parent-name"><span class="mark"></span>TAVMONT</p>
    </div>
  </section>

  <section class="card card-back" aria-label="Card back">
    <div class="brand">BLUE<br>FORGE</div>
    <div class="services">
      <span>Medical Training</span><span class="dot"></span>
      <span>Consultancy</span><span class="dot"></span>
      <span>Executive Protection Courses</span>
    </div>
  </section>
</main>
</body>
</html>
```